Corvane Lending Partners. Professional and Established Company

A full service finance company specializing in obtaining capital for small business. Business Lending advisor, helping small business owners access the capital they need to launch, grow, or sustain their business. Many of our programs offer flexible guidelines to overcome common obstacles such as credit score, credit history, and time in business, financials, and industry type. Our streamlined funding process makes getting a business loan, business line of credit, stated income commercial real estate loan, a smooth and stress free experience.SOME OF THE MOST COMMON NEEDS FOR BUSINESS CAPITAL:• Working Capital• Debt Consolidations (loans, merchant cash advances, etc.)• Payroll• Operating Expenses• Inventory• Equipment Financing• Commercial Real Estate (Purchase, Fix & Flip, Rehab, Renovations)• Business Acquisitions• Business ExpansionWe like the websites:www.brookfellcap.com they are in the same industry and provide the same servicesWe are wanting to be able to update when we do press releases and such using Word Press. Our look should be very professional and we will be adding Our Team Professional Bios and Headshots.

Industry/Entity Type

Finance

Number of Pages Required

5+ page

Font styles to use
Serif
Sans Serif

Requirements
Must have
• We want to copy brookfellcap.com
• We need:
• Home Page
• About Us
• Loan Programs
• Loan Criteria
• News
• Apply Now
• Contact
Nice to have
• See brookfellcap.com
Should not have
• Need professional design. Nothing bright or abstract

```html
<!DOCTYPE html>
<html lang="en">
<head>
<meta charset="utf-8">
<title>Corvane Lending Partners</title>
<link href="https://fonts.googleapis.com/css2?family=Cinzel:wght@400;700&family=Open+Sans:wght@400;600;700&display=swap" rel="stylesheet">
<style>
:root{
  --blue:#2b6eb5;
  --blue-dark:#1f5a99;
  --ink:#222;
  --text:#555;
  --light:#eceff1;
  --grey-btn:#6d6d6d;
  --dark:#2b2b2b;
  --white:#fff;
}
*{box-sizing:border-box;margin:0;padding:0}
html,body{width:1200px;height:3991px;overflow:hidden}
body{font-family:"Open Sans",Arial,sans-serif;color:var(--text);background:var(--white);position:relative}
.abs{position:absolute}
section,header,nav,footer{position:absolute;left:0;width:1200px}
.serif{font-family:"Cinzel","Times New Roman",serif}

/* header */
.top{top:0;height:93px;background:var(--white)}
.brand{left:146px;top:18px;width:260px;color:var(--blue);font-family:"Cinzel",serif;font-size:22px;font-weight:700;line-height:1.15}
.contact-item{top:26px;display:flex;align-items:center;gap:12px;font-size:12px;color:#555;line-height:1.35}
.contact-item .ic{width:26px;height:26px;border-radius:50%;background:#e9eef4;display:flex;align-items:center;justify-content:center}
.contact-item span b{color:var(--blue);font-weight:400;display:block}
.quote-btn{left:945px;top:29px;width:114px;height:35px;background:var(--grey-btn);color:#fff;font-size:13px;font-weight:700;display:flex;align-items:center;justify-content:center;letter-spacing:.5px}

/* nav */
.mainnav{top:93px;height:43px;background:var(--blue)}
.mainnav a{position:absolute;top:0;height:43px;line-height:43px;color:#fff;font-size:12.5px;text-decoration:none;transform:translateX(-50%);letter-spacing:.3px}
.mainnav a.active{background:#6b7e93;padding:0 22px}

/* hero */
.hero{top:136px;height:534px;background:linear-gradient(180deg,#1e2f44 0%,#3b5a7d 40%,#6d8fb3 75%,#8fb2d4 100%)}
.hero h1{position:absolute;left:0;width:1200px;top:176px;text-align:center;color:#fff;font-family:"Cinzel",serif;font-weight:700;font-size:31px;line-height:1.32;text-shadow:0 2px 6px rgba(0,0,0,.45)}
.hero .cta{left:519px;top:316px;width:162px;height:38px;background:var(--blue);color:#fff;font-size:13px;font-weight:700;display:flex;align-items:center;justify-content:center;border:1px solid #7fb0e6}
.hero .dot{left:52px;top:249px;width:28px;height:28px;border-radius:50%;border:1px solid rgba(255,255,255,.7)}

/* headings */
.sec-title{position:absolute;left:0;width:1200px;text-align:center;font-family:"Cinzel",serif;font-size:31px;color:var(--ink);letter-spacing:1px}
.sec-title em{font-style:normal;color:var(--blue)}
.sec-rule{position:absolute;left:540px;width:120px;height:1px;background:#c9d3dd}

/* about */
.about{top:670px;height:384px}
.about .lead{left:230px;width:740px;top:152px;text-align:center;color:var(--blue);font-weight:700;font-size:16px;line-height:1.65}
.about .body{left:260px;width:680px;top:217px;text-align:center;font-size:12.5px;line-height:1.7}
.btn-small{background:var(--blue);color:#fff;font-size:13px;display:flex;align-items:center;justify-content:center}

/* closed loans */
.closed{top:1054px;height:394px;background:var(--light)}
.loan-card{top:154px;width:243px;height:162px;background:#fff;text-align:center;padding-top:30px;box-shadow:0 2px 8px rgba(0,0,0,.12)}
.loan-card h4{font-family:"Cinzel",serif;font-weight:400;font-size:15px;color:var(--ink);letter-spacing:.5px}
.loan-card .amt{font-family:"Cinzel",serif;font-size:31px;color:var(--ink);margin-top:8px}
.loan-card p{font-size:12px;margin-top:8px}
.loan-card.featured{background:var(--blue)}
.loan-card.featured h4{font-family:"Open Sans",sans-serif;font-weight:700;font-size:13px;color:#fff}
.loan-card.featured .amt,.loan-card.featured p{color:#fff}
.arrow{width:32px;height:32px;border-radius:50%;background:#fff;border:1px solid #ccc;display:flex;align-items:center;justify-content:center}

/* news */
.news{top:1448px;height:726px}
.news-row{left:0;width:1200px;height:282px}
.news-text{background:rgba(30,90,160,.88);color:#fff;padding:38px 56px 0 56px}
.news-text h3{font-family:"Cinzel",serif;font-weight:400;font-size:19.5px;line-height:1.35;letter-spacing:.4px}
.news-text p{font-size:12px;line-height:1.75;margin-top:12px;color:#e3ecf7}
.news-text a{display:block;margin-top:8px;color:#fff;font-weight:700;font-size:13px;text-decoration:none}
.photo-city{background:linear-gradient(160deg,#b9cfe4 0%,#5e86b0 45%,#2a4d78 100%)}
.photo-building{background:linear-gradient(180deg,#3b6fa6 0%,#5d86b3 45%,#c79a5e 75%,#3d4450 100%)}

/* loan programs */
.programs{top:2174px;height:546px;background:#eef0f2}
.prog{display:flex;align-items:center;gap:22px;font-family:"Cinzel",serif;font-size:19px;color:var(--ink);line-height:1.2}
.prog .icon{width:64px;height:64px;border-radius:50%;background:var(--blue);flex:none;display:flex;align-items:center;justify-content:center}

/* team */
.team{top:2720px;height:585px}
.member{top:159px;width:261px;height:341px}
.member .photo{position:absolute;left:0;top:0;width:261px;height:279px}
.member .cap{position:absolute;left:0;top:279px;width:261px;height:62px;background:#dfe4e6;text-align:center;padding-top:10px}
.member .cap h5{font-family:"Cinzel",serif;font-weight:400;font-size:14px;color:var(--ink)}
.member .cap p{font-size:11px;margin-top:4px}
.member.open .cap{top:192px;height:170px;background:var(--blue);color:#fff;padding-top:26px}
.member.open .cap h5,.member.open .cap p{color:#fff}
.member.open .cap .line{display:flex;align-items:center;gap:12px;justify-content:flex-start;padding-left:20px;font-size:12px;margin-top:12px;text-align:left}
.member.open .cap .line.big{font-size:16px;font-weight:700}
.chev{position:absolute;left:112px;top:-18px;width:36px;height:36px;border-radius:50%;background:var(--blue);display:flex;align-items:center;justify-content:center}

/* contact */
.contact{top:3305px;height:439px;background:linear-gradient(90deg,#4a4a4a 0%,#2d2d2d 60%,#3a3a3a 100%)}
.contact .sec-title{color:#fff}
.contact .logo{left:146px;top:157px;color:#cfcfcf;font-family:"Cinzel",serif;font-size:28px;line-height:1.1;width:260px}
.contact .info{left:146px;color:#eee;font-size:12px;display:flex;gap:16px;align-items:flex-start;line-height:1.5}
.climber{right:0;top:40px;width:470px;height:399px;background:linear-gradient(200deg,rgba(120,120,120,.35),rgba(20,20,20,.6))}
.field{left:777px;width:269px;height:32px;border:1px solid #9a9a9a;background:rgba(0,0,0,.25);color:#ddd;font-size:11.5px;padding:8px 10px}
.submit{left:773px;top:3653px;width:111px;height:36px;background:var(--blue);border:1px solid #8fbbe9;color:#fff;font-family:"Cinzel",serif;font-size:16px;display:flex;align-items:center;justify-content:center}

.map{top:3744px;height:205px;background:linear-gradient(180deg,#dcdcdc,#cfd2d4)}
.map-label{left:447px;top:82px;width:118px;height:46px;background:#fff;border:1px solid #bbb;color:var(--blue);font-family:"Cinzel",serif;font-size:11px;font-weight:700;display:flex;align-items:center;justify-content:center;text-align:center;line-height:1.15}

.foot{top:3949px;height:42px;background:var(--blue);color:#fff;font-size:12px}
.foot .copy{left:146px;top:13px}
.foot .soc{top:10px;width:22px;height:22px;border-radius:50%;background:#fff}
</style>
</head>
<body>

<header class="top">
  <div class="abs brand">Corvane Lending Partners</div>
  <div class="abs contact-item" style="left:514px">
    <div class="ic"><svg width="12" height="12" viewBox="0 0 24 24"><path fill="#2b6eb5" d="M6.6 10.8a15 15 0 0 0 6.6 6.6l2.2-2.2c.3-.3.7-.4 1-.2 1.1.4 2.3.6 3.6.6.6 0 1 .4 1 1V20c0 .6-.4 1-1 1A17 17 0 0 1 3 4c0-.6.4-1 1-1h3.5c.6 0 1 .4 1 1 0 1.3.2 2.5.6 3.6.1.3 0 .7-.2 1z"/></svg></div>
    <span><b>Call Us</b>303-555-0148</span>
  </div>
  <div class="abs contact-item" style="left:682px">
    <div class="ic"><svg width="13" height="10" viewBox="0 0 24 18"><rect x="1" y="1" width="22" height="16" fill="#2b6eb5"/><path d="M1 1l11 9 11-9" stroke="#fff" stroke-width="2" fill="none"/></svg></div>
    <span><b>Email On</b>info@corvanelending.com</span>
  </div>
  <div class="abs quote-btn">GET A QUOTE</div>
</header>

<nav class="mainnav">
  <a class="active" href="#" style="left:192px">HOME</a>
  <a href="#" style="left:330px">ABOUT US</a>
  <a href="#" style="left:474px">LOAN PROGRAMS</a>
  <a href="#" style="left:639px">LOAN CRITERIA</a>
  <a href="#" style="left:758px">NEWS</a>
  <a href="#" style="left:873px">APPLY NOW</a>
  <a href="#" style="left:1006px">CONTACT US</a>
</nav>

<section class="hero" role="img" aria-label="Upward view of glass office towers against a blue sky">
  <div class="abs dot"></div>
  <h1>WE ARE FULL SERVICE FINANCE COMPANY<br>SPECIALIZING IN OBTAINING CAPITAL<br>FOR SMALL BUSINESS.</h1>
  <div class="abs cta">CONTACT US TODAY</div>
</section>

<section class="about">
  <h2 class="sec-title" style="top:66px">ABOUT <em>CORVANE</em></h2>
  <div class="sec-rule" style="top:122px"></div>
  <p class="abs lead">As a leading business lender helping business owners access the capital needed to launch, grow, and develop their business.</p>
  <p class="abs body">Corvane Lending overcomes common obstacles such as credit issues, various industries, business history, and financials. Corvane brings decades of experience in Finance, Lending, and the Energy Industry to help secure all sizes of loans for all purposes.</p>
  <div class="abs btn-small" style="left:543px;top:300px;width:113px;height:33px">Read More</div>
</section>

<section class="closed">
  <h2 class="sec-title" style="top:66px">RECENTLY <em>CLOSED LOANS</em></h2>
  <div class="sec-rule" style="top:120px"></div>
  <div class="abs arrow" style="left:163px;top:219px"><svg width="8" height="12" viewBox="0 0 8 12"><path d="M6 1L1 6l5 5" stroke="#666" stroke-width="2" fill="none"/></svg></div>
  <div class="abs loan-card" style="left:237px"><h4>OPERATING CAPITAL</h4><div class="amt">$ 1,500,000</div><p>Construction</p></div>
  <div class="abs loan-card featured" style="left:480px"><h4>ACQUISITION</h4><div class="amt">$ 511,000</div><p>Medical Practice</p></div>
  <div class="abs loan-card" style="left:723px"><h4>COMMERCIAL REAL ESTATE</h4><div class="amt">$ 2,100,000</div><p>Refinance</p></div>
  <div class="abs arrow" style="left:1000px;top:219px"><svg width="8" height="12" viewBox="0 0 8 12"><path d="M2 1l5 5-5 5" stroke="#666" stroke-width="2" fill="none"/></svg></div>
</section>

<section class="news">
  <h2 class="sec-title" style="top:72px">LATEST <em>NEWS</em></h2>
  <div class="sec-rule" style="top:126px"></div>
  <div class="abs news-row" style="top:151px">
    <div class="abs photo-city" style="left:0;top:0;width:1200px;height:282px" role="img" aria-label="Glass office towers seen from street level"></div>
    <div class="abs news-text" style="left:0;top:0;width:812px;height:282px">
      <h3>PROIN EUISMOD, EST MOLLIS TEMPOR CONVALLIS, MASSA IPSUM SEMPER EX, AT MATTIS SEM VELIT MATTIS ARCU.</h3>
      <p>Etiam lacinia ullamcorper sapien, ut sollicitudin metus maximus a. Aliquam ut nulla eu urna luctus tincidunt. In at sodales est, sed porta justo. Integer ac neque id ante lacinia consequat dapibus vel est. Morbi accumsan tellus a volutpat venenatis. Phasellus volutpat odio nec libero elementum pretium. Etiam laoreet eros tellus, at pretium eros consectetur ac. Nunc at condimentum eros, eget mattis ipsum.</p>
      <a href="#">Read More....</a>
    </div>
  </div>
  <div class="abs news-row" style="top:433px">
    <div class="abs photo-building" style="left:0;top:0;width:1200px;height:282px" role="img" aria-label="Modern glass office building at dusk"></div>
    <div class="abs news-text" style="left:389px;top:0;width:811px;height:282px;padding-left:36px">
      <h3>PROIN EUISMOD, EST MOLLIS TEMPOR CONVALLIS, MASSA IPSUM SEMPER EX, AT MATTIS SEM VELIT MATTIS ARCU.</h3>
      <p>Etiam lacinia ullamcorper sapien, ut sollicitudin metus maximus a. Aliquam ut nulla eu urna luctus tincidunt. In at sodales est, sed porta justo. Integer ac neque id ante lacinia consequat dapibus vel est. Morbi accumsan tellus a volutpat venenatis. Phasellus volutpat odio nec libero elementum pretium. Etiam laoreet eros tellus, at pretium eros consectetur ac. Nunc at condimentum eros, eget mattis ipsum.</p>
      <a href="#">Read More....</a>
    </div>
  </div>
</section>

<section class="programs">
  <h2 class="sec-title" style="top:60px">LOAN <em>PROGRAMS</em></h2>
  <div class="sec-rule" style="top:114px"></div>

  <div class="abs prog" style="left:149px;top:149px"><div class="icon"><svg width="34" height="30" viewBox="0 0 34 30"><rect x="3" y="4" width="28" height="22" rx="3" fill="none" stroke="#fff" stroke-width="2"/><path d="M8 20l6-8 5 5 3-3 5 6z" fill="#fff"/></svg></div>Land Loans</div>
  <div class="abs prog" style="left:460px;top:149px"><div class="icon"><svg width="34" height="26" viewBox="0 0 34 26"><path d="M2 13l8-7 7 4 7-4 8 7-8 7-7-3-7 3z" fill="none" stroke="#fff" stroke-width="2"/><path d="M12 12l5 3 5-3" stroke="#fff" stroke-width="2" fill="none"/></svg></div>Office Loans</div>
  <div class="abs prog" style="left:772px;top:149px"><div class="icon"><svg width="34" height="30" viewBox="0 0 34 30"><path d="M3 26V14l8-5v5l8-5v5l8-5v17z" fill="#fff"/><rect x="26" y="3" width="4" height="10" fill="#fff"/></svg></div>Industrial Loans</div>

  <div class="abs prog" style="left:149px;top:269px"><div class="icon"><svg width="28" height="32" viewBox="0 0 28 32"><rect x="7" y="6" width="14" height="24" fill="#fff"/><rect x="12" y="1" width="4" height="5" fill="#fff"/><rect x="2" y="16" width="5" height="14" fill="#fff"/><rect x="21" y="16" width="5" height="14" fill="#fff"/></svg></div>Hospitality<br>Loans</div>
  <div class="abs prog" style="left:460px;top:269px"><div class="icon"><svg width="30" height="30" viewBox="0 0 30 30"><rect x="4" y="3" width="22" height="25" fill="none" stroke="#fff" stroke-width="2"/><path d="M8 9h14M8 14h14M8 19h14M8 24h8" stroke="#fff" stroke-width="2"/></svg></div>Mixed-use Loans</div>
  <div class="abs prog" style="left:772px;top:269px"><div class="icon"><svg width="34" height="28" viewBox="0 0 34 28"><rect x="2" y="8" width="18" height="12" fill="#fff"/><path d="M20 11h7l5 5v4H20z" fill="#fff"/><circle cx="9" cy="23" r="3" fill="#fff"/><circle cx="26" cy="23" r="3" fill="#fff"/></svg></div>Warehouse Loans</div>

  <div class="abs prog" style="left:149px;top:391px"><div class="icon"><svg width="34" height="30" viewBox="0 0 34 30"><path d="M3 14L17 4l14 10" stroke="#fff" stroke-width="2.5" fill="none"/><rect x="7" y="14" width="20" height="13" fill="#fff"/></svg></div>Multifamily<br>Loans</div>
  <div class="abs prog" style="left:460px;top:391px"><div class="icon"><svg width="30" height="30" viewBox="0 0 30 30"><path d="M15 4v22M7 26h16" stroke="#fff" stroke-width="2"/><path d="M5 9h20" stroke="#fff" stroke-width="2"/><path d="M2 18l3-9 3 9zM22 18l3-9 3 9z" fill="#fff"/></svg></div>Retail Loans</div>
</section>

<section class="team">
  <h2 class="sec-title" style="top:72px">OUR <em>TEAM</em></h2>
  <div class="sec-rule" style="top:126px"></div>
  <div class="abs arrow" style="left:104px;top:290px"><svg width="8" height="12" viewBox="0 0 8 12"><path d="M6 1L1 6l5 5" stroke="#666" stroke-width="2" fill="none"/></svg></div>

  <div class="abs member open" style="left:186px">
    <div class="photo" style="background:linear-gradient(180deg,#8c8f93,#5b5f66)" role="img" aria-label="Headshot of executive director"></div>
    <div class="cap">
      <div class="chev"><svg width="12" height="8" viewBox="0 0 12 8"><path d="M1 7l5-5 5 5" stroke="#fff" stroke-width="2" fill="none"/></svg></div>
      <h5>Lauren K. Ashby</h5>
      <p>Executive Director</p>
      <div class="line big"><svg width="14" height="14" viewBox="0 0 24 24"><path fill="#fff" d="M6.6 10.8a15 15 0 0 0 6.6 6.6l2.2-2.2c.3-.3.7-.4 1-.2 1.1.4 2.3.6 3.6.6.6 0 1 .4 1 1V20c0 .6-.4 1-1 1A17 17 0 0 1 3 4c0-.6.4-1 1-1h3.5c.6 0 1 .4 1 1 0 1.3.2 2.5.6 3.6.1.3 0 .7-.2 1z"/></svg>303-555-0172</div>
      <div class="line"><svg width="14" height="10" viewBox="0 0 24 18"><rect x="1" y="1" width="22" height="16" fill="#fff"/><path d="M1 1l11 9 11-9" stroke="#2b6eb5" stroke-width="2" fill="none"/></svg>lauren@corvanelending.com</div>
    </div>
  </div>

  <div class="abs member" style="left:468px">
    <div class="photo" style="background:linear-gradient(180deg,#3e4f63,#1c2836)" role="img" aria-label="Headshot of chief marketing officer"></div>
    <div class="cap"><h5>Daniel R. Hollis</h5><p>Chief Marketing Officer</p></div>
  </div>

  <div class="abs member" style="left:750px">
    <div class="photo" style="background:linear-gradient(180deg,#b9aa98,#8a7a68)" role="img" aria-label="Headshot of regional sales director"></div>
    <div class="cap"><h5>Megan Castell</h5><p>Regional Sales Director</p></div>
  </div>

  <div class="abs arrow" style="left:1057px;top:290px"><svg width="8" height="12" viewBox="0 0 8 12"><path d="M2 1l5 5-5 5" stroke="#666" stroke-width="2" fill="none"/></svg></div>
</section>

<section class="contact">
  <div class="abs climber" role="img" aria-label="Silhouette of climbers helping each other up a rock face"></div>
  <h2 class="sec-title" style="top:66px">CONTACT US</h2>
  <div class="sec-rule" style="top:120px;background:#777"></div>
  <div class="abs logo">Corvane Lending Partners</div>
  <div class="abs info" style="top:273px"><svg width="12" height="16" viewBox="0 0 12 16"><path d="M6 0a6 6 0 0 1 6 6c0 4-6 10-6 10S0 10 0 6a6 6 0 0 1 6-6z" fill="#fff"/><circle cx="6" cy="6" r="2" fill="#333"/></svg><span><b>CORVANE LENDING PARTNERS</b><br>4120 Alder Ridge Ct, Denver, CO 80203</span></div>
  <div class="abs info" style="top:327px"><svg width="14" height="10" viewBox="0 0 24 18"><rect x="1" y="1" width="22" height="16" fill="#fff"/><path d="M1 1l11 9 11-9" stroke="#333" stroke-width="2" fill="none"/></svg><span>info@corvanelending.com</span></div>
  <div class="abs info" style="top:360px"><svg width="13" height="13" viewBox="0 0 24 24"><path fill="#fff" d="M6.6 10.8a15 15 0 0 0 6.6 6.6l2.2-2.2c.3-.3.7-.4 1-.2 1.1.4 2.3.6 3.6.6.6 0 1 .4 1 1V20c0 .6-.4 1-1 1A17 17 0 0 1 3 4c0-.6.4-1 1-1h3.5c.6 0 1 .4 1 1 0 1.3.2 2.5.6 3.6.1.3 0 .7-.2 1z"/></svg><span>303-555-0148</span></div>
</section>
<div class="abs field" style="top:3455px">Name</div>
<div class="abs field" style="top:3497px">Email</div>
<div class="abs field" style="top:3537px;display:flex;justify-content:space-between">Inquiry For<span>&#9662;</span></div>
<div class="abs field" style="top:3578px;height:56px">Your Message</div>
<div class="abs submit">Submit</div>

<section class="map" role="img" aria-label="Street map around the office location">
  <div class="abs map-label">Corvane Lending Partners</div>
  <svg class="abs" style="left:574px;top:78px" width="24" height="32" viewBox="0 0 12 16"><path d="M6 0a6 6 0 0 1 6 6c0 4-6 10-6 10S0 10 0 6a6 6 0 0 1 6-6z" fill="#2b6eb5"/><circle cx="6" cy="6" r="2" fill="#fff"/></svg>
</section>

<footer class="foot">
  <div class="abs copy">Copyright © 2018 CORVANE LENDING PARTNERS . All Rights Reserved.</div>
  <div class="abs soc" style="left:944px"></div>
  <div class="abs soc" style="left:972px"></div>
  <div class="abs soc" style="left:1000px"></div>
  <div class="abs soc" style="left:1028px"></div>
</footer>

</body>
</html>
```